Web Design for "Global Broadcasting Service Business"

We are a satellite company launching a new exciting brand by the name of "Velorun". Velorun is a broadcasting solution provider that gives end-to-end solutions to TV channels and other content providers to deliver and distribute their content globally. Weather it be TV channels that need to be broadcasted in their local regions or internationally, or its collection of news from various locations, or even coverage of special sports or other events, we provide the technology and services to make that happen. This allows the broadcaster to focus on the content rather than worry about the logistics of how it will get to its viewers. We can help place their content to regional cable and satellite operators. Moreover we can provide services for content creation and coverage of major sports, news and special events. Velorun is one-stop-shop for all broadcast solutions

We want a 20 page static website. I am mentioning certain key competitors of ours so that you can have a look at the comparable look we are anticipating in the design

www.orbavex.tv
www.skarnello.com
www.pivarrum.com

Its a global company so the design has to give the same look and feel

Target Market(s)

TV Channel Owners and their Technical Heads

Industry/Entity Type

Business

Requirements
Must have
• We want the designers to submit the home page design first giving us the look and feel of the website design. you can use sample text and any satellite based image to start off. Once we shortlist the best home page designs we will ask you to create the remaining pages.

The most work is on the home page, remaining subsections will only require a change in text and images at most. the overall look and feel of the website including headers and footers will remain the same

```html
<!DOCTYPE html>
<html lang="en">
<head>
<meta charset="utf-8">
<title>Velorun — Regional Solution, Global Distribution</title>
<link href="https://fonts.googleapis.com/css2?family=Lato:wght@400;700;900&family=Montserrat:wght@400;800&family=Open+Sans:wght@400;600&display=swap" rel="stylesheet">
<style>
:root{
  --red:#b5001d;
  --red-bright:#d0021b;
  --ink:#1a1a1a;
  --grey:#666;
  --light:#f3f3f3;
  --line:#cfcfcf;
  --blue:#1f6fc1;
  --nav:#1c1c1c;
  --footer:#000;
}
*{box-sizing:border-box;margin:0;padding:0}
html,body{width:946px;height:1200px;overflow:hidden}
body{position:relative;font-family:"Lato",sans-serif;color:var(--ink);background:#fff}
a{color:inherit;text-decoration:none}
.abs{position:absolute}

.topbar{position:absolute;left:0;top:0;width:946px;height:27px;background:var(--red);color:#fff;font-size:10.5px}
.topbar .util{position:absolute;left:135px;top:7px;display:flex;gap:0}
.topbar .util a{padding:0 6px;border-left:1px solid rgba(255,255,255,.5)}
.topbar .util a:first-child{padding-left:0;border:0}
.topbar .account{position:absolute;right:134px;top:6px;display:flex;gap:18px;font-size:12px;align-items:center}
.topbar .account span{display:flex;align-items:center;gap:4px}

.header{position:absolute;left:0;top:27px;width:946px;height:91px;background:#fff}
.brand{position:absolute;left:136px;top:22px;display:flex;align-items:center;gap:6px}
.brand .dot{width:12px;height:12px;border-radius:50%;background:var(--red)}
.brand .name{font-family:"Lato",sans-serif;font-weight:900;font-size:38px;color:var(--ink);letter-spacing:-.5px;line-height:1}
.tagline{position:absolute;left:140px;top:70px;font-size:7.5px;font-weight:700}
.connect{position:absolute;right:136px;top:12px;display:flex;align-items:center;gap:5px}
.connect b{color:var(--red);font-size:9.5px;margin-right:6px}
.connect i{width:20px;height:20px;border-radius:50%;background:#9a9a9a;display:block}
.search{position:absolute;left:642px;top:51px;width:169px;height:26px;border:1px solid #ddd;background:#f4f4f4;font-size:10px;color:#999;padding:7px 6px}
.search .btn{position:absolute;right:0;top:0;width:28px;height:24px;border-left:1px solid #ddd;background:#eee}

.mainnav{position:absolute;left:0;top:118px;width:946px;height:33px;background:linear-gradient(#2d2d2d,#0e0e0e);display:flex;align-items:center;padding-left:135px}
.mainnav a{color:#fff;font-size:9.6px;font-weight:700;letter-spacing:-.2px;padding:0 10px;border-left:1px solid #555;line-height:12px}
.mainnav a:first-child{padding-left:0;border:0}

.hero{position:absolute;left:0;top:151px;width:946px;height:379px;background:linear-gradient(180deg,#5a7390 0%,#8b9fb4 35%,#b7c2cc 60%,#77766e 82%,#5b4d3a 100%)}
.hero-headline{position:absolute;left:146px;top:236px;font-family:"Montserrat",sans-serif;line-height:1}
.hero-headline .l1{font-size:52px;font-weight:400;color:#fff;letter-spacing:-2px}
.hero-headline .l2{font-size:49px;font-weight:800;color:var(--red);letter-spacing:-2px;margin-top:2px}
.readmore{position:absolute;left:148px;top:351px;width:100px;height:27px;background:#1e1e1e;color:#fff;font-family:"Montserrat",sans-serif;font-weight:800;font-size:13px;letter-spacing:-.5px;text-align:center;line-height:27px}

.news{position:absolute;left:0;top:530px;width:946px;height:166px;background:var(--light)}
.sec-title{position:absolute;display:flex;align-items:center;gap:7px;font-size:17px;color:var(--red);letter-spacing:-.4px}
.news .rule{position:absolute;left:135px;top:41px;width:676px;height:1px;background:var(--line)}
.arrows{position:absolute;left:772px;top:19px;display:flex;gap:3px}
.arrows i{width:17px;height:14px;background:var(--red-bright);display:flex;align-items:center;justify-content:center}
.card{position:absolute;top:73px;width:215px;height:64px}
.card .thumb{position:absolute;left:0;top:0;width:100px;height:64px;border:2px solid #ccc}
.card .meta{position:absolute;left:106px;top:0;width:110px}
.card .date{display:flex;align-items:center;gap:3px;color:var(--red);font-size:9px;font-weight:700;margin-top:2px}
.card h4{color:var(--blue);font-size:8.4px;font-weight:900;margin-top:9px}
.card p{color:#888;font-size:8.2px;line-height:11px;margin-top:3px}
.vsep{position:absolute;top:52px;width:1px;height:108px;background:#e0e0e0}

.lower{position:absolute;left:0;top:696px;width:946px;height:270px;background:radial-gradient(ellipse at 70% 55%,#f4f4f5 0%,#e6e8ec 40%,#c9cfd8 100%)}
.lower .rule{position:absolute;height:1px;background:#b8bcc4}
.event{position:absolute;left:135px;width:442px}
.event .cal{position:absolute;left:0;top:-2px}
.event h5{position:absolute;left:39px;top:0;font-family:"Open Sans",sans-serif;font-size:9px;font-weight:600}
.event p{position:absolute;left:39px;top:13px;width:403px;font-family:"Open Sans",sans-serif;font-size:8.2px;line-height:12px;color:#555}
.lower .vline{position:absolute;left:590px;top:22px;width:1px;height:222px;background:#b8bcc4}
.field-label{position:absolute;left:601px;font-size:12.5px;letter-spacing:-.3px}
.field{position:absolute;left:601px;width:211px;height:24px;background:#dfe1e4;border:1px solid #c5c8cc}
.subscribe{position:absolute;left:681px;top:194px;width:130px;height:30px;background:var(--red-bright);color:#fff;font-size:18px;letter-spacing:-.5px;display:flex;align-items:center;justify-content:center;gap:8px}

.footer{position:absolute;left:0;top:972px;width:946px;height:228px;background:var(--footer);color:#fff}
.fcol{position:absolute;top:32px}
.fcol h6{font-size:11px;font-weight:400;letter-spacing:-.3px;padding-bottom:6px;border-bottom:2px solid #555;width:124px}
.fcol ul{list-style:none;margin-top:12px}
.fcol li{font-size:8.3px;line-height:14.4px;letter-spacing:-.2px}
.footer .rule{position:absolute;left:135px;top:164px;width:676px;height:1px;background:#444}
.copy{position:absolute;left:136px;top:184px;font-size:9.5px;color:#ccc}
.legal{position:absolute;left:136px;top:206px;font-size:9.5px;color:#ccc}
.fbrand{position:absolute;right:136px;top:182px;display:flex;align-items:center;gap:6px}
.fbrand .dot{width:10px;height:10px;border-radius:50%;background:#fff}
.fbrand .name{font-weight:900;font-size:32px;letter-spacing:-.5px;line-height:1}
</style>
</head>
<body>

<div class="topbar">
  <nav class="util"><a href="#">Home</a><a href="#">Careers</a><a href="#">Contact Us</a><a href="#">About</a></nav>
  <div class="account">
    <span><svg width="10" height="11" viewBox="0 0 10 11"><circle cx="5" cy="3" r="2.6" fill="#fff"/><path d="M0 11c0-3.5 2-5 5-5s5 1.5 5 5z" fill="#fff"/></svg>Login</span>
    <span><svg width="14" height="10" viewBox="0 0 14 10"><rect x=".5" y=".5" width="13" height="9" fill="none" stroke="#fff"/><path d="M.5.5 7 6 13.5.5" fill="none" stroke="#fff"/></svg>Contact Us</span>
  </div>
</div>

<header class="header">
  <div class="brand"><span class="dot"></span><span class="name">Velorun</span></div>
  <div class="tagline">Regional Solution, Global Distribution</div>
  <div class="connect"><b>CONNECT US :</b><i></i><i></i><i></i><i></i></div>
  <div class="search">Search
    <span class="btn"><svg width="28" height="24" viewBox="0 0 28 24"><circle cx="13" cy="11" r="5" fill="none" stroke="#555" stroke-width="1.5"/><path d="M16.5 14.5 20 18" stroke="#555" stroke-width="2"/></svg></span>
  </div>
</header>

<nav class="mainnav">
  <a href="#">HOME</a><a href="#">WHO WE ARE</a><a href="#">BROADCAST SOLUTIONS</a><a href="#">REGIONAL DISTRIBUTION</a><a href="#">ON-DEMAND SERVICES</a><a href="#">GLOBAL NETWORK</a><a href="#">BEAMS</a>
</nav>

<section class="hero" role="img" aria-label="Large white satellite dish antenna under a cloudy blue sky, with more dishes across a plain in the distance"></section>
<div class="hero-headline"><div class="l1">Deliver Reliable</div><div class="l2">BROADCASTER</div></div>
<a class="readmore" href="#">READ MORE</a>

<section class="news">
  <div class="sec-title" style="left:135px;top:16px">
    <svg width="18" height="17" viewBox="0 0 18 17"><rect x="1" y="1" width="16" height="11" fill="none" stroke="#222" stroke-width="1.6"/><path d="M6 16h6M9 12v4" stroke="#222" stroke-width="1.6"/><circle cx="9" cy="6" r="2" fill="#222"/></svg>News</div>
  <div class="arrows">
    <i><svg width="8" height="8" viewBox="0 0 8 8"><path d="M5.5 1 2.5 4l3 3" fill="none" stroke="#fff" stroke-width="2"/></svg></i>
    <i><svg width="8" height="8" viewBox="0 0 8 8"><path d="M2.5 1l3 3-3 3" fill="none" stroke="#fff" stroke-width="2"/></svg></i>
  </div>
  <div class="rule"></div>

  <article class="card" style="left:135px">
    <div class="thumb" role="img" aria-label="Crowd gathered around a dark car on a street" style="background:linear-gradient(#3c4656,#1f2633)"></div>
    <div class="meta"><div class="date"><svg width="15" height="13" viewBox="0 0 15 13"><rect x=".7" y="1.7" width="13.6" height="10.6" fill="#fff" stroke="#222" stroke-width="1.2"/><rect x=".7" y="1.7" width="13.6" height="3" fill="#222"/></svg>2014-01-29</div>
    <h4>DAS JAHR DER RENTNER</h4><p>Die positiven Nachrichten in Bezug auf die Rente halten</p></div>
  </article>
  <div class="vsep" style="left:356px"></div>
  <article class="card" style="left:368px">
    <div class="thumb" role="img" aria-label="Monster truck jumping high above a crowd" style="background:linear-gradient(#f2f3f4 60%,#9aa08e)"></div>
    <div class="meta"><div class="date"><svg width="15" height="13" viewBox="0 0 15 13"><rect x=".7" y="1.7" width="13.6" height="10.6" fill="#fff" stroke="#222" stroke-width="1.2"/><rect x=".7" y="1.7" width="13.6" height="3" fill="#222"/></svg>2014-01-29</div>
    <h4>DAS JAHR DER RENTNER</h4><p>Die positiven Nachrichten in Bezug auf die Rente halten</p></div>
  </article>
  <div class="vsep" style="left:589px"></div>
  <article class="card" style="left:602px">
    <div class="thumb" role="img" aria-label="Crowd of spectators on a snowy hillside under a blue sky" style="background:linear-gradient(#2f6bb8 0%,#8fb1d8 45%,#5b6a80 100%)"></div>
    <div class="meta"><div class="date"><svg width="15" height="13" viewBox="0 0 15 13"><rect x=".7" y="1.7" width="13.6" height="10.6" fill="#fff" stroke="#222" stroke-width="1.2"/><rect x=".7" y="1.7" width="13.6" height="3" fill="#222"/></svg>2014-01-29</div>
    <h4>DAS JAHR DER RENTNER</h4><p>Die positiven Nachrichten in Bezug auf die Rente halten</p></div>
  </article>
</section>

<section class="lower" role="img" aria-label="Soft pale cloudy sky background">
  <div class="sec-title" style="left:135px;top:31px">
    <svg width="18" height="17" viewBox="0 0 18 17"><rect x="1" y="1" width="16" height="11" fill="none" stroke="#222" stroke-width="1.6"/><path d="M6 16h6M9 12v4" stroke="#222" stroke-width="1.6"/><circle cx="9" cy="6" r="2" fill="#222"/></svg>Upcomming Events</div>
  <div class="rule" style="left:135px;top:58px;width:436px"></div>

  <div class="event" style="top:80px">
    <svg class="cal" width="31" height="31" viewBox="0 0 31 31"><rect x="1.2" y="4.2" width="28.6" height="25.6" rx="2" fill="#fff" stroke="#c8102e" stroke-width="2.4"/><rect x="1.2" y="4.2" width="28.6" height="6" fill="#c8102e"/><path d="M8 1v6M23 1v6" stroke="#c8102e" stroke-width="2.4"/><text x="15.5" y="25" text-anchor="middle" font-family="Lato,sans-serif" font-size="11" fill="#c8102e">29</text></svg>
    <h5>SATELLITE 2014</h5>
    <p>Lorem Ipsum is simply dummy text of the printing and typesetting industry. Lorem Ipsum has been the industry's standard dummy text ever since the 1500s,</p>
  </div>
  <div class="rule" style="left:135px;top:126px;width:436px"></div>
  <div class="event" style="top:136px">
    <svg class="cal" width="31" height="31" viewBox="0 0 31 31"><rect x="1.2" y="4.2" width="28.6" height="25.6" rx="2" fill="#fff" stroke="#c8102e" stroke-width="2.4"/><rect x="1.2" y="4.2" width="28.6" height="6" fill="#c8102e"/><path d="M8 1v6M23 1v6" stroke="#c8102e" stroke-width="2.4"/><text x="15.5" y="25" text-anchor="middle" font-family="Lato,sans-serif" font-size="11" fill="#c8102e">10</text></svg>
    <h5>SATELLITE 2014</h5>
    <p>Lorem Ipsum is simply dummy text of the printing and typesetting industry. Lorem Ipsum has been the industry's standard dummy text ever since the 1500s,</p>
  </div>
  <div class="rule" style="left:135px;top:180px;width:436px"></div>
  <div class="event" style="top:190px">
    <svg class="cal" width="31" height="31" viewBox="0 0 31 31"><rect x="1.2" y="4.2" width="28.6" height="25.6" rx="2" fill="#fff" stroke="#c8102e" stroke-width="2.4"/><rect x="1.2" y="4.2" width="28.6" height="6" fill="#c8102e"/><path d="M8 1v6M23 1v6" stroke="#c8102e" stroke-width="2.4"/><text x="15.5" y="25" text-anchor="middle" font-family="Lato,sans-serif" font-size="11" fill="#c8102e">01</text></svg>
    <h5>SATELLITE 2014</h5>
    <p>Lorem Ipsum is simply dummy text of the printing and typesetting industry. Lorem Ipsum has been the industry's standard dummy text ever since the 1500s,</p>
  </div>

  <div class="vline"></div>

  <div class="sec-title" style="left:601px;top:31px">
    <svg width="20" height="18" viewBox="0 0 20 18"><path d="M1.5 1.5h17v11H8l-4 4v-4H1.5z" fill="none" stroke="#222" stroke-width="1.6"/><path d="M5 5.5h10M5 8.5h10" stroke="#222" stroke-width="1.4"/></svg>Newsletter</div>
  <div class="rule" style="left:601px;top:58px;width:210px"></div>
  <div class="field-label" style="top:78px">Name*</div>
  <div class="field" style="top:97px"></div>
  <div class="field-label" style="top:131px">E-mail*</div>
  <div class="field" style="top:150px"></div>
  <a class="subscribe" href="#"><svg width="16" height="16" viewBox="0 0 16 16"><rect width="16" height="16" rx="3" fill="#fff"/><circle cx="4.5" cy="11.5" r="1.6" fill="#d0021b"/><path d="M3 7.5a5.5 5.5 0 0 1 5.5 5.5M3 4a9 9 0 0 1 9 9" fill="none" stroke="#d0021b" stroke-width="1.8"/></svg>Subscribe</a>
</section>

<footer class="footer">
  <div class="fcol" style="left:135px"><h6>LINKS</h6><ul><li>Home</li><li>How We Are</li><li>Broadcast Solution</li><li>Regional Distribution</li><li>On-Demand Services</li><li>More Link</li></ul></div>
  <div class="fcol" style="left:311px"><h6>BROADCAST SOLUTIONS</h6><ul><li>Teleport Facilities</li><li>Turnaround</li><li>MCPC Platforms</li><li>HD/3D Playout Center</li></ul></div>
  <div class="fcol" style="left:487px"><h6>REGIONAL DISTRIBUTION</h6><ul><li>Access to Cable &amp; DTH head ends</li><li>Market Analysis Consultancy</li></ul></div>
  <div class="fcol" style="left:661px"><h6 style="width:150px">ON-DEMAND SERVICES</h6><ul><li>Coverage of News, Sports &amp; Special Events</li><li>HD/3D Transmission Services</li><li>Satellite Usage Capacity</li><li>Master Control Room</li></ul></div>
  <div class="rule"></div>
  <div class="copy">2014 © Velorun.All Rights Reserved .</div>
  <div class="legal">Privacy Policy &nbsp;| &nbsp;Sitemap &nbsp;| &nbsp;Terms &amp; Condition</div>
  <div class="fbrand"><span class="dot"></span><span class="name">Velorun</span></div>
</footer>

</body>
</html>
```